Speisekarten-Design für Café
Vielen lieben Dank!
Zielgruppe
Café mit Angebot von Frühstück und Torten/Kuchen (BIO!) und Verkauf von Dekoartikeln. Zielgruppe sind sowohl Familien, als auch ältere Personen, die sich zum Kaffeeklatsch treffen. Ebenso 'Freundinnen' und junge Mütter.
In den Räumlichkeiten war schon seit 24 Jahren ein Café, die Besitzerin ist aber verstorben
Aufgabenstellung
Karte in DIN A 5 Format, da die Tische nicht so groß sind. Die erste Seite soll die 'Geschichte' der Lokalität enthalten. Keine 'bunten' Bilder (Comics) von irgendwelchen Torten und/oder Frühstücken

```html
<!DOCTYPE html>
<html lang="de">
<head>
<meta charset="utf-8">
<title>Speisekarte – Tassenglück</title>
<link href="https://fonts.googleapis.com/css2?family=Great+Vibes&family=Merriweather:wght@300;400&display=swap" rel="stylesheet">
<style>
  :root {
    --berry: #a7317a;
    --berry-light: #b25089;
    --berry-edge: #8e2a67;
    --ink: #222220;
    --paper: #ffffff;
    --text: #3a3a3a;
    --badge-ring: #5b4a40;
    --icon: #8a7a70;
  }
  * { margin: 0; padding: 0; box-sizing: border-box; }
  html, body { width: 1200px; height: 568px; overflow: hidden; background: var(--paper); }
  body { position: relative; font-family: "Merriweather", Georgia, serif; font-weight: 300; }

  .stripes {
    position: absolute;
    background: repeating-linear-gradient(90deg, var(--berry) 0 8px, var(--berry-light) 8px 16px);
  }
  .cover-stripes { left: 0; top: 0; width: 400px; height: 149px; }
  .cover-rule { position: absolute; left: 0; top: 149px; width: 400px; height: 5px; background: var(--ink); }
  .inside-stripes { left: 400px; top: 0; width: 400px; height: 446px; border-left: 1px solid var(--berry-edge); border-right: 1px solid var(--berry-edge); }

  .berry-band { position: absolute; top: 446px; height: 5px; background: var(--berry); }
  .band-left { left: 0; width: 400px; }
  .band-right { left: 800px; width: 400px; }

  .footer { position: absolute; left: 0; top: 451px; width: 1200px; height: 117px; background: var(--ink); }

  .script { font-family: "Great Vibes", cursive; font-weight: 400; }

  .cover-title {
    position: absolute; left: 0; width: 400px; top: 196px; text-align: center;
    font-size: 84px; color: var(--berry); line-height: 1;
  }
  .cover-subtitle {
    position: absolute; left: 0; width: 400px; top: 261px; text-align: center;
    font-size: 9.5px; color: var(--text); letter-spacing: 0.2px;
  }

  .welcome-title {
    position: absolute; left: 400px; width: 400px; top: 118px; text-align: center;
    font-size: 48px; line-height: 43px; color: var(--paper);
  }
  .welcome-text {
    position: absolute; left: 400px; width: 400px; top: 216px; text-align: center;
    font-size: 9px; line-height: 16.3px; color: var(--paper);
  }

  .about-title {
    position: absolute; left: 800px; width: 400px; top: 120px; text-align: center;
    font-size: 46px; color: var(--berry); line-height: 1;
  }
  .about-text {
    position: absolute; left: 881px; width: 236px; top: 172px;
    font-size: 9.4px; line-height: 16.2px; color: var(--text);
    text-align: justify; hyphens: auto;
  }

  .badge {
    position: absolute; width: 104px; height: 104px; border-radius: 50%;
    background: var(--paper); border: 2px solid var(--badge-ring);
    display: flex; align-items: center; justify-content: center;
    font-size: 11px; color: var(--ink); font-weight: 400;
  }
  .badge-cover { left: 148px; top: 362px; }
  .badge-inside { left: 548px; top: 362px; }

  .hours {
    position: absolute; left: 400px; width: 400px; top: 483px; text-align: center;
    font-size: 9.5px; color: var(--paper); font-weight: 400;
  }
  .hours sup { font-size: 5.5px; }
  .contact-lines { position: absolute; left: 572px; top: 518px; font-size: 7.5px; line-height: 11.5px; color: var(--paper); }
  .contact-line { display: flex; align-items: center; gap: 5px; }
  .contact-line svg { width: 7px; height: 7px; }

  .footer-mark {
    position: absolute; left: 832px; top: 485px; width: 54px; height: 54px; border-radius: 50%;
    border: 1px solid var(--berry); display: flex; align-items: center; justify-content: center;
    font-size: 6.5px; color: var(--berry);
  }
  .address { position: absolute; left: 916px; top: 504px; font-size: 7.5px; line-height: 11.5px; color: var(--berry); }
  .web { position: absolute; left: 1046px; top: 504px; font-size: 7.5px; line-height: 11.5px; color: var(--berry); }
  .web-line { display: flex; align-items: center; gap: 5px; }
  .dot { width: 6px; height: 6px; border-radius: 50%; background: var(--berry); display: inline-block; }
</style>
</head>
<body>
  <!-- Cover panel -->
  <div class="stripes cover-stripes"></div>
  <div class="cover-rule"></div>
  <h1 class="script cover-title">Speisekarte</h1>
  <p class="cover-subtitle">Frühstück &amp; Getränke</p>

  <!-- Inside panel -->
  <div class="stripes inside-stripes"></div>
  <h2 class="script welcome-title">Genießen Sie<br>Ihre Zeit bei uns!</h2>
  <p class="welcome-text">Bitte sagen Sie uns,<br>wenn Sie etwas vermissen. Für Anregungen, durch die<br>wir Ihren Besuch in unserem Café noch genussvoller<br>machen können, sind wir dankbar.</p>

  <!-- About panel -->
  <h2 class="script about-title">Über uns</h2>
  <p class="about-text">Lorem ipsum dolor sit amet, consetetur sadipscing elitr, sed diam nonumy eirmod tempor invidunt ut labore et dolore magna aliquyam erat, sed diam voluptua. At vero eos et accusam et justo duo dolores et ea rebum. Stet clita kasd gubergren, no sea takimata sanctus est Lorem ipsum dolor sit amet. Lorem ipsum dolor sit amet, consetetur sadipscing elitr, sed diam nonumy eirmod tempor invidunt ut labore et dolore magna aliquyam erat, sed diam voluptua. At vero eos et accusam et justo duo dolores et ea rebum. Stet clita kasd gubergren, no sea takimata sanctus est Lorem ipsum dolor sit amet.</p>

  <!-- Bands & footer -->
  <div class="berry-band band-left"></div>
  <div class="berry-band band-right"></div>
  <footer class="footer"></footer>

  <div class="badge badge-cover">Tassenglück</div>
  <div class="badge badge-inside">Tassenglück</div>

  <p class="hours">Unsere Öffnungszeiten: täglich 8 bis 13 Uhr und 14<sup>30</sup> bis 18 Uhr</p>
  <div class="contact-lines">
    <div class="contact-line">
      <svg viewBox="0 0 10 10" aria-label="Telefon"><circle cx="5" cy="5" r="5" fill="var(--icon)"/><path d="M3 2.5c0 2.5 2 4.8 4.5 5l.6-1-1.3-.8-.6.6c-.9-.4-1.6-1.1-2-2l.6-.6-.8-1.3z" fill="#fff"/></svg>
      <span>0 12 34 . 567 89 00</span>
    </div>
    <div class="contact-line">
      <svg viewBox="0 0 10 10" aria-label="Fax"><circle cx="5" cy="5" r="5" fill="var(--icon)"/><rect x="3" y="3.5" width="4" height="3.5" fill="#fff"/></svg>
      <span>0 12 34 . 567 89 00</span>
    </div>
  </div>

  <div class="footer-mark">Tassenglück</div>
  <div class="address">Lindenallee 17<br>31234 Musterstadt</div>
  <div class="web">
    <div class="web-line"><span class="dot"></span><span>tassenglueck.de</span></div>
    <div class="web-line"><span class="dot"></span><span>@tassenglueck</span></div>
  </div>
</body>
</html>
```